We need a web design for a new hair care company that is based in Israel but exports its line of products around the world. We would like special features on this website that include video, sliders and other exciting effects. The final design should present information about the products and an exciting inviting image. We also will need to know how to update the site.

Designers can look at our current website and see the colors and look of the products as well. Please go to: http://lunoveltresses.com

We would like to use the colors of the Lunovel Tresses care line of products. Wordpress seems to be a good choice. We would like four pages: Home, About Us, Contact and Products.

If designers have specific questions.....please let us know!
Let the designs begin!!!!
We are waiting and excited!

Target Market(s)

Potential haircare distributors and general public

Industry/Entity Type

Hair

Requirements
Must have
• The website must have general info about what the company is, with a video, explain how to use each product and a focus on women and hair.
Nice to have
• On the website should be the logo, product info, upbeat music, video and sliders that show the exciting world of Lunovel Tresscare. It's uniqueness is that it offers Dead Sea minerals for the hair, the first of its kind.

```html
<!DOCTYPE html>
<html lang="en">
<head>
<meta charset="utf-8">
<title>Lunovel Tresscare – Contact Us</title>
<link rel="stylesheet" href="https://fonts.googleapis.com/css2?family=Open+Sans:wght@300;400;600&display=swap">
<style>
  :root {
    --turquoise: #3ebfd8;
    --turquoise-deep: #2aa7c2;
    --brown: #5a2e12;
    --brown-dark: #3f1e0a;
    --tan: #c09a6b;
    --white: #ffffff;
    --ink: #1a1a1a;
    --photo-dark: #1c1410;
    --photo-mid: #5b3a26;
    --photo-light: #9a7a62;
  }
  * { box-sizing: border-box; margin: 0; padding: 0; }
  html, body { width: 1200px; height: 900px; overflow: hidden; background: var(--white); }
  body { font-family: "Open Sans", Arial, sans-serif; position: relative; }

  .page-backdrop {
    position: absolute; left: 0; top: 214px; width: 1200px; height: 609px;
    background: var(--tan);
  }
  .pattern-band {
    position: absolute; left: 0; top: 105px; width: 1200px; height: 67px;
    background: linear-gradient(90deg, var(--turquoise) 0%, #8a6a3f 18%, var(--turquoise) 36%, #8a6a3f 55%, var(--turquoise) 72%, #8a6a3f 88%, var(--turquoise) 100%);
  }
  .nav-bar {
    position: absolute; left: 0; top: 172px; width: 1200px; height: 42px;
    background: var(--brown);
  }
  .brand-box {
    position: absolute; left: 164px; top: 105px; width: 262px; height: 173px;
    background: var(--turquoise);
    display: flex; align-items: center; justify-content: center;
    z-index: 3;
  }
  .brand-name {
    font-weight: 300; font-size: 42px; color: var(--brown); letter-spacing: 1px;
  }
  .main-nav {
    position: absolute; left: 432px; top: 172px; height: 42px;
    display: flex; align-items: center; z-index: 3;
  }
  .main-nav a {
    color: var(--white); text-decoration: none; font-size: 13px;
    padding: 0 12px; line-height: 22px; white-space: nowrap;
    border-left: 1px solid rgba(255,255,255,0.7);
  }
  .main-nav a:first-child { border-left: none; }
  .main-nav a.is-active { color: var(--turquoise); }
  .social-links {
    position: absolute; left: 978px; top: 186px; display: flex; gap: 12px; z-index: 3;
  }
  .social-links span {
    width: 15px; height: 15px; border-radius: 50%; background: var(--white); display: block;
  }

  .hero-photo {
    position: absolute; left: 120px; top: 214px; width: 980px; height: 571px;
    background:
      radial-gradient(ellipse 30% 45% at 45% 35%, var(--photo-light) 0%, rgba(154,122,98,0) 70%),
      radial-gradient(ellipse 60% 70% at 70% 60%, var(--photo-mid) 0%, rgba(91,58,38,0) 75%),
      linear-gradient(100deg, #cfcac6 0%, #7a6a60 12%, var(--photo-dark) 45%, #3a2618 70%, #bdb6b0 100%);
  }

  .contact-info {
    position: absolute; left: 190px; top: 614px; color: var(--white); z-index: 2;
  }
  .contact-title {
    font-weight: 400; font-size: 26px; line-height: 30px; color: var(--turquoise); margin-bottom: 12px;
  }
  .contact-columns { display: flex; gap: 0; font-size: 13px; line-height: 18px; }
  .contact-columns p { width: 210px; }

  .contact-form { position: absolute; left: 686px; top: 342px; width: 332px; z-index: 2; }
  .form-label {
    display: block; color: var(--turquoise-deep); font-size: 12px; line-height: 16px;
  }
  .form-field {
    display: block; width: 330px; height: 30px; border: none; border-radius: 3px;
    background: var(--white); margin-bottom: 16px; font-family: inherit;
  }
  .form-field.is-message { height: 122px; margin-bottom: 12px; resize: none; }
  .send-button {
    position: absolute; right: 0; bottom: -30px;
    width: 42px; height: 26px; border: none; border-radius: 3px;
    background: var(--white); color: var(--turquoise-deep);
    font-family: inherit; font-size: 13px;
  }
</style>
</head>
<body>
  <div class="page-backdrop"></div>
  <div class="pattern-band" role="img" aria-label="Decorative paisley band in turquoise and brown"></div>
  <div class="nav-bar"></div>

  <header>
    <div class="brand-box"><span class="brand-name">Lunovel</span></div>
    <nav class="main-nav">
      <a href="#">Home</a>
      <a href="#">About Us</a>
      <a href="#">Our Products</a>
      <a href="#">Lookbook</a>
      <a href="#">Video</a>
      <a href="#" class="is-active">Contact Us</a>
    </nav>
    <div class="social-links">
      <span aria-label="Social link"></span>
      <span aria-label="Social link"></span>
      <span aria-label="News feed link"></span>
    </div>
  </header>

  <main>
    <div class="hero-photo" role="img" aria-label="Photograph of a woman with long, glossy dark brown hair sweeping across the frame"></div>

    <section class="contact-info">
      <h1 class="contact-title">Contact Us</h1>
      <div class="contact-columns">
        <p>Lunovel Tresscare<br>418 Harbor Lane<br>Marin Bay, CA 94000</p>
        <p>lunoveltresscare.com<br>Tel 555-014-2368<br>Fax 555-014-2369</p>
      </div>
    </section>

    <form class="contact-form">
      <label class="form-label" for="name">Name</label>
      <input class="form-field" id="name" type="text">
      <label class="form-label" for="email">Email</label>
      <input class="form-field" id="email" type="email">
      <label class="form-label" for="subject">Subject</label>
      <input class="form-field" id="subject" type="text">
      <label class="form-label" for="message">Message</label>
      <textarea class="form-field is-message" id="message"></textarea>
      <button class="send-button" type="button">Send</button>
    </form>
  </main>
</body>
</html>
```